Graphic Design Project Van Signage

Hi there, the project is to use the attached icons to create a modern, sophisticated & clean looking mobile advertisement on the side of a van.
The Business is called Qorvanta & we provide service in the fields of:
-Electrical
-Security
-Audio-Visual
-Data & Voice

I would like designers to use the icons (provided) & Qorvanta logo (provided) to develop a design on the silver Renault Traffic LWB. This design needs to depict the services we provide (see 4 fields above) in such a way, that a prospective client understands (from the advertisement) that the business automates the process of electrical services.

It is most important that the Icons remain in high res quality & must have smooth lines.
Also attached is a picture of two of the vans to assist designers in visualising the look we are aiming to present to perspective clients which is, clean, elegant & a well run business, please take this look consideration when submitting designs.
When designing please use a large side & rear picture of the Silver Renault Traffic Van (not supplied) there is no design required for the front of the Van

Do Not ! use any of the images from my web site, I am looking for a new concept
Updates

Project Deadline Extended
Reason: Hi there everyone thank you for all your designs, at this time I would like to draw your attention back to the design brief, I am looking for a clean professional look of graphic design, you may check out the previous designs at www.qorvanta-example.com.au but again please do not copy this design but rather take note of the simplistic clean design, the current project is to invent a new design incorporating the icons available in the brief to advertise in logo form the services available for Qorvanta, I thank you for the designs so far but feel that I have not seen any striking designs that make me stop

Industry/Entity Type

Electrical

Requirements
Must have
• Must have the following discreetly & placed on both sides of the van & be 150mm high "REC 48302"
Nice to have
• (w) www.qorvanta-example.com.au
(e) sales@qorvanta-example.com.au
(m) 0400 512 364
Should not have
• no design for the front bonnet of the van required
Do Not use any of the images from my web site, I am looking for a new concept

```html
<!DOCTYPE html>
<html lang="en">
<head>
<meta charset="utf-8">
<title>Qorvanta Van Signage</title>
<link rel="stylesheet" href="https://fonts.googleapis.com/css2?family=Cormorant+Garamond:wght@400&family=Open+Sans:wght@400&display=swap">
<style>
  :root {
    --bg: #ffffff;
    --ink: #4a4a4c;
    --ink-soft: #6d6d70;
    --accent: #7ac943;
    --icon-grey: #5a5a5c;
    --caption: #555555;
  }
  * { margin: 0; padding: 0; box-sizing: border-box; }
  html, body { width: 1200px; height: 413px; overflow: hidden; background: var(--bg); }
  .canvas { position: relative; width: 1200px; height: 413px; }
  .icon-layer { position: absolute; left: 0; top: 0; width: 1200px; height: 413px; }
  .i-green { color: var(--accent); }
  .i-grey { color: var(--icon-grey); }
  .wordmark { position: absolute; font-family: "Cormorant Garamond", serif; font-weight: 400; color: var(--ink); font-size: 46px; line-height: 1; letter-spacing: 1px; white-space: nowrap; }
  .tagline { position: absolute; font-family: "Cormorant Garamond", serif; color: var(--ink); font-size: 10px; letter-spacing: 1.4px; white-space: nowrap; }
  .web { position: absolute; font-family: "Open Sans", sans-serif; color: var(--ink-soft); font-size: 5px; letter-spacing: 1px; text-transform: uppercase; white-space: nowrap; }
  .contact { position: absolute; display: flex; gap: 8px; font-family: "Open Sans", sans-serif; font-size: 7px; color: var(--ink); align-items: center; }
  .contact__item { display: flex; align-items: center; gap: 3px; white-space: nowrap; }
  .contact__icon { width: 8px; height: 8px; }
  .licence { position: absolute; font-family: "Open Sans", sans-serif; font-size: 6px; letter-spacing: 0.5px; color: var(--ink-soft); white-space: nowrap; }
  .caption { position: absolute; left: 0; width: 1200px; top: 360px; text-align: center; font-family: "Open Sans", sans-serif; font-size: 12px; letter-spacing: 0.6px; color: var(--caption); }
</style>
</head>
<body>
<div class="canvas">

  <svg class="icon-layer" viewBox="0 0 1200 413" aria-hidden="true">
    <defs>
      <symbol id="bulb" viewBox="0 0 24 24"><circle cx="12" cy="9" r="7" fill="currentColor"/><rect x="8.5" y="16" width="7" height="2.2" fill="currentColor"/><rect x="9" y="19" width="6" height="2.2" fill="currentColor"/></symbol>
      <symbol id="phone" viewBox="0 0 24 24"><path d="M5 3h4l2 5-2.5 1.8a12 12 0 0 0 5.7 5.7L16 13l5 2v4a2 2 0 0 1-2 2A17 17 0 0 1 3 5a2 2 0 0 1 2-2z" fill="currentColor"/></symbol>
      <symbol id="camera" viewBox="0 0 24 24"><rect x="2" y="6" width="16" height="7" rx="1.5" fill="currentColor"/><path d="M18 8l4-2v7l-4-2z" fill="currentColor"/><rect x="8" y="13" width="2.5" height="5" fill="currentColor"/><rect x="4" y="18" width="10" height="2.5" fill="currentColor"/></symbol>
      <symbol id="speaker" viewBox="0 0 24 24"><rect x="5" y="2" width="14" height="20" rx="2" fill="currentColor"/><circle cx="12" cy="7" r="2" fill="#fff"/><circle cx="12" cy="15" r="4" fill="#fff"/><circle cx="12" cy="15" r="1.6" fill="currentColor"/></symbol>
      <symbol id="home" viewBox="0 0 24 24"><path d="M2 12L12 3l10 9h-3v9h-5v-6h-4v6H5v-9z" fill="currentColor"/></symbol>
      <symbol id="tablet" viewBox="0 0 24 24"><rect x="5" y="2" width="14" height="20" rx="2" fill="none" stroke="currentColor" stroke-width="2"/><circle cx="12" cy="19" r="1" fill="currentColor"/></symbol>
      <symbol id="laptop" viewBox="0 0 24 24"><rect x="4" y="5" width="16" height="11" rx="1" fill="none" stroke="currentColor" stroke-width="2"/><rect x="1" y="17" width="22" height="2.5" rx="1" fill="currentColor"/></symbol>
      <symbol id="wifi" viewBox="0 0 24 24"><path d="M3 9a13 13 0 0 1 18 0M6 12.5a8.5 8.5 0 0 1 12 0M9 16a4 4 0 0 1 6 0" fill="none" stroke="currentColor" stroke-width="2.2" stroke-linecap="round"/><circle cx="12" cy="19.5" r="1.6" fill="currentColor"/></symbol>
      <symbol id="siren" viewBox="0 0 24 24"><path d="M6 18v-5a6 6 0 0 1 12 0v5z" fill="currentColor"/><rect x="4" y="18" width="16" height="3" fill="currentColor"/><path d="M12 2v3M4 6l2 2M20 6l-2 2M1 12h3M20 12h3" stroke="currentColor" stroke-width="1.8" stroke-linecap="round"/></symbol>
      <symbol id="monitor" viewBox="0 0 24 24"><rect x="2" y="3" width="20" height="13" rx="1" fill="none" stroke="currentColor" stroke-width="2"/><rect x="10" y="16" width="4" height="3" fill="currentColor"/><rect x="7" y="19" width="10" height="2" fill="currentColor"/></symbol>
    </defs>

    <!-- left side: main cluster -->
    <g class="icons-left-main">
      <use href="#siren" class="i-grey" x="468" y="90" width="22" height="22"/>
      <use href="#phone" class="i-green" x="498" y="92" width="18" height="18"/>
      <use href="#wifi" class="i-green" x="527" y="110" width="22" height="22"/>
      <use href="#bulb" class="i-green" x="450" y="118" width="26" height="26"/>
      <use href="#phone" class="i-grey" x="480" y="116" width="20" height="20"/>
      <use href="#camera" class="i-grey" x="502" y="118" width="22" height="22"/>
      <use href="#bulb" class="i-green" x="456" y="146" width="22" height="22"/>
      <use href="#speaker" class="i-grey" x="483" y="142" width="22" height="22"/>
      <use href="#tablet" class="i-grey" x="508" y="148" width="20" height="20"/>
      <use href="#home" class="i-grey" x="530" y="135" width="22" height="22"/>
      <use href="#home" class="i-green" x="531" y="160" width="18" height="18"/>
      <use href="#laptop" class="i-grey" x="456" y="170" width="24" height="24"/>
      <use href="#monitor" class="i-grey" x="485" y="176" width="20" height="20"/>
      <use href="#home" class="i-green" x="438" y="188" width="18" height="18"/>
      <use href="#phone" class="i-green" x="508" y="178" width="18" height="18"/>
      <use href="#tablet" class="i-grey" x="529" y="193" width="22" height="22"/>
      <use href="#laptop" class="i-grey" x="470" y="198" width="18" height="18"/>
    </g>
    <!-- left side: small cluster -->
    <g class="icons-left-small">
      <use href="#siren" class="i-grey" x="210" y="172" width="16" height="16"/>
      <use href="#home" class="i-grey" x="234" y="170" width="16" height="16"/>
      <use href="#bulb" class="i-green" x="193" y="190" width="18" height="18"/>
      <use href="#speaker" class="i-grey" x="214" y="190" width="18" height="18"/>
      <use href="#home" class="i-green" x="240" y="192" width="16" height="16"/>
      <use href="#wifi" class="i-green" x="174" y="214" width="16" height="16"/>
      <use href="#phone" class="i-green" x="192" y="210" width="15" height="15"/>
      <use href="#laptop" class="i-grey" x="206" y="228" width="18" height="18"/>
      <use href="#tablet" class="i-grey" x="230" y="226" width="16" height="16"/>
      <use href="#home" class="i-green" x="249" y="220" width="16" height="16"/>
      <use href="#monitor" class="i-grey" x="168" y="234" width="16" height="16"/>
    </g>

    <!-- right side: main cluster -->
    <g class="icons-right-main">
      <use href="#siren" class="i-grey" x="710" y="90" width="22" height="22"/>
      <use href="#phone" class="i-green" x="684" y="92" width="18" height="18"/>
      <use href="#wifi" class="i-green" x="651" y="110" width="22" height="22"/>
      <use href="#bulb" class="i-green" x="724" y="118" width="26" height="26"/>
      <use href="#phone" class="i-grey" x="700" y="116" width="20" height="20"/>
      <use href="#camera" class="i-grey" x="676" y="118" width="22" height="22"/>
      <use href="#bulb" class="i-green" x="722" y="146" width="22" height="22"/>
      <use href="#speaker" class="i-grey" x="695" y="142" width="22" height="22"/>
      <use href="#tablet" class="i-grey" x="672" y="148" width="20" height="20"/>
      <use href="#home" class="i-grey" x="648" y="135" width="22" height="22"/>
      <use href="#home" class="i-green" x="651" y="160" width="18" height="18"/>
      <use href="#laptop" class="i-grey" x="720" y="170" width="24" height="24"/>
      <use href="#monitor" class="i-grey" x="695" y="176" width="20" height="20"/>
      <use href="#home" class="i-green" x="744" y="188" width="18" height="18"/>
      <use href="#phone" class="i-green" x="674" y="178" width="18" height="18"/>
      <use href="#tablet" class="i-grey" x="649" y="193" width="22" height="22"/>
      <use href="#laptop" class="i-grey" x="712" y="198" width="18" height="18"/>
    </g>
    <!-- right side: small cluster -->
    <g class="icons-right-small">
      <use href="#siren" class="i-grey" x="944" y="172" width="16" height="16"/>
      <use href="#home" class="i-grey" x="967" y="170" width="16" height="16"/>
      <use href="#bulb" class="i-green" x="1004" y="188" width="18" height="18"/>
      <use href="#speaker" class="i-grey" x="983" y="188" width="18" height="18"/>
      <use href="#home" class="i-green" x="960" y="190" width="16" height="16"/>
      <use href="#wifi" class="i-green" x="1025" y="206" width="16" height="16"/>
      <use href="#phone" class="i-green" x="1008" y="208" width="15" height="15"/>
      <use href="#laptop" class="i-grey" x="986" y="212" width="18" height="18"/>
      <use href="#tablet" class="i-grey" x="1030" y="226" width="16" height="16"/>
      <use href="#home" class="i-green" x="966" y="212" width="16" height="16"/>
      <use href="#monitor" class="i-grey" x="1010" y="230" width="16" height="16"/>
    </g>
  </svg>

  <div class="wordmark" style="left:295px; top:134px">Qorvanta</div>
  <div class="tagline" style="left:305px; top:190px">Electrical Security AV</div>
  <div class="web" style="left:320px; top:206px">www.qorvanta-example.com.au</div>
  <div class="contact" style="left:295px; top:237px">
    <span class="contact__item">
      <svg class="contact__icon" viewBox="0 0 8 8"><rect width="8" height="8" fill="var(--icon-grey)"/><path d="M2 2 L3 2 L3.6 3.4 L3 4 Q4 5 5 5 L5.6 4.4 L6.6 5 L6.6 6 Q3 6.2 2 2Z" fill="var(--accent)"/></svg>
      0400 512 364
    </span>
    <span class="contact__item">
      <svg class="contact__icon" viewBox="0 0 8 8"><rect width="8" height="8" fill="var(--icon-grey)"/><rect x="1.5" y="2.3" width="5" height="3.6" fill="none" stroke="var(--accent)" stroke-width="0.7"/><path d="M1.5 2.3 L4 4.3 L6.5 2.3" fill="none" stroke="var(--accent)" stroke-width="0.7"/></svg>
      sales@qorvanta-example.com.au
    </span>
  </div>
  <div class="licence" style="left:295px; top:252px">REC 48302</div>

  <div class="wordmark" style="left:760px; top:134px">Qorvanta</div>
  <div class="tagline" style="left:770px; top:190px">Electrical Security AV</div>
  <div class="web" style="left:785px; top:206px">www.qorvanta-example.com.au</div>
  <div class="contact" style="left:770px; top:237px">
    <span class="contact__item">
      <svg class="contact__icon" viewBox="0 0 8 8"><rect width="8" height="8" fill="var(--icon-grey)"/><path d="M2 2 L3 2 L3.6 3.4 L3 4 Q4 5 5 5 L5.6 4.4 L6.6 5 L6.6 6 Q3 6.2 2 2Z" fill="var(--accent)"/></svg>
      0400 512 364
    </span>
    <span class="contact__item">
      <svg class="contact__icon" viewBox="0 0 8 8"><rect width="8" height="8" fill="var(--icon-grey)"/><rect x="1.5" y="2.3" width="5" height="3.6" fill="none" stroke="var(--accent)" stroke-width="0.7"/><path d="M1.5 2.3 L4 4.3 L6.5 2.3" fill="none" stroke="var(--accent)" stroke-width="0.7"/></svg>
      sales@qorvanta-example.com.au
    </span>
  </div>
  <div class="licence" style="left:770px; top:252px">REC 48302</div>

  <p class="caption">GRAPHIC&nbsp; ICONS WITHOUT A BACKGROUND STRAIGHT ONTO THE VAN</p>
</div>
</body>
</html>
```